Carpal Tunnel - PPC Landing Page

We need to do a SINGLE page landing page for a doctor who specializes in Carpal Tunnel syndrome - please research if you're not familiar - it's very common.

Landing page essentials:
Must have a form in upper right hand corner:
Form title: "Get a free diagnosis."
Form inputs: Name, Phone, Email, Requested Appointment time

Page is for PPC, so needs to be simple and light on content. Content has been provided and attached to this project.

No navigation, just a single page.

Industry/Entity Type

Health

Coding

Coded - Design and coding required

Number of Pages Required

1 page

Requirements
Must have
• Elegant look - Conversion optimized for form and phone
• Responsive design.
Should not have
• Old outdated images.

```html
<!DOCTYPE html>
<html lang="en">
<head>
<meta charset="utf-8">
<title>Dr. Halvern — Carpal Tunnel Care</title>
<link href="https://fonts.googleapis.com/css2?family=Open+Sans:ital,wght@0,400;0,600;0,700;1,700&display=swap" rel="stylesheet">
<style>
:root{
  --blue:#1e8ee0;
  --blue-dark:#1476c2;
  --teal:#2b7b7a;
  --teal-light:#7fe3d6;
  --red:#c8102e;
  --ink:#333;
  --muted:#666;
  --hero-bg:#e9f1f8;
  --grey-bg:#ececec;
  --white:#fff;
}
*{box-sizing:border-box;margin:0;padding:0}
html,body{width:796px;height:1200px;overflow:hidden}
body{font-family:"Open Sans",Arial,sans-serif;color:var(--ink);background:var(--white);position:relative}

.site-header{height:50px;display:flex;align-items:center;justify-content:space-between;padding:0 22px;background:var(--white)}
.brand-name{font-size:25px;font-weight:700;color:var(--blue);line-height:1}
.brand-tagline{font-size:6px;color:var(--muted);letter-spacing:.5px;margin-top:2px;text-transform:uppercase}
.header-phone{display:flex;align-items:center;gap:8px;font-size:19px;font-weight:600;color:var(--blue)}
.header-phone .icon{width:26px;height:26px;border-radius:50%;background:var(--blue);display:flex;align-items:center;justify-content:center}

.hero{height:315px;position:relative;background:linear-gradient(90deg,#f3f7fb 0%,var(--hero-bg) 45%,#dbe8f4 100%);overflow:hidden}
.hero-visual{position:absolute;left:160px;top:0;width:400px;height:315px}
.lead-form{position:absolute;left:596px;top:22px;width:176px;height:258px;background:var(--white);box-shadow:0 2px 8px rgba(0,0,0,.18);padding:16px 12px}
.lead-form h2{font-size:15px;font-weight:700;color:#444;text-transform:uppercase;line-height:1.15;margin-bottom:12px}
.lead-form h2 em{font-style:normal;color:var(--red)}
.lead-form .field{height:22px;border:1px solid #ccc;margin-bottom:8px;font-size:8px;color:#666;padding:5px 6px;border-radius:2px}
.lead-form .submit{display:block;width:70px;height:24px;margin:14px auto 0;background:var(--red);color:var(--white);border:0;border-radius:3px;font-size:9px;font-weight:700;text-transform:uppercase;font-family:inherit}

.about{height:235px;background:var(--teal);position:relative;color:var(--white)}
.about h2{text-align:center;font-size:30px;font-weight:400;padding-top:30px}
.about h2 span{color:var(--teal-light)}
.about-art{position:absolute;left:44px;top:115px;width:160px;height:65px;border-radius:30px 8px 8px 30px;background:linear-gradient(90deg,#f2d5c0,#dcb49a)}
.about-text{position:absolute;left:232px;top:108px;width:540px;font-size:8.5px;line-height:1.6;color:#d9efee}
.about-text p+p{margin-top:8px}

.conditions{height:315px;position:relative}
.conditions h2{position:absolute;left:34px;top:40px;font-size:20px;font-weight:700;text-transform:uppercase;color:#222}
.conditions h2 span{color:var(--blue)}
.condition-list{position:absolute;left:40px;top:103px;width:370px;display:grid;grid-template-columns:1fr 1fr;row-gap:22px;list-style:none}
.condition-list li{display:flex;align-items:center;gap:10px;font-size:10.5px;color:#333}
.condition-list .num{width:20px;height:20px;border-radius:50%;background:var(--blue);color:var(--white);font-size:10px;font-weight:700;display:flex;align-items:center;justify-content:center;flex:none}
.doctor-photo{position:absolute;left:545px;top:32px;width:215px;height:283px;background:linear-gradient(180deg,#f4f4f4,#d9dde2)}

.location{height:260px;background:var(--grey-bg);position:relative}
.map{position:absolute;left:30px;top:22px;width:350px;height:215px;background:linear-gradient(135deg,#e6e4dc,#d5dccb)}
.address{position:absolute;left:452px;top:25px;width:320px}
.address h3{font-size:13px;font-weight:700;color:var(--blue);text-transform:uppercase;margin-bottom:12px}
.address-row{display:flex;gap:9px;font-size:9px;line-height:1.55;color:#444;margin-bottom:8px}
.address-row svg{flex:none;margin-top:2px}

.site-footer{position:absolute;left:0;bottom:0;width:796px;height:25px;background:var(--blue);color:var(--white);font-size:7px;text-align:center;line-height:25px}
</style>
</head>
<body>

<header class="site-header">
  <div class="brand">
    <div class="brand-name">Dr. Halvern</div>
    <div class="brand-tagline">Hand &amp; wrist care specialist</div>
  </div>
  <div class="header-phone">
    <span class="icon"><svg width="13" height="13" viewBox="0 0 24 24"><path fill="#fff" d="M6.6 10.8a15.1 15.1 0 0 0 6.6 6.6l2.2-2.2c.3-.3.7-.4 1-.2 1.1.4 2.3.6 3.6.6.6 0 1 .4 1 1V20c0 .6-.4 1-1 1A17 17 0 0 1 3 4c0-.6.4-1 1-1h3.5c.6 0 1 .4 1 1 0 1.3.2 2.5.6 3.6.1.3 0 .7-.2 1z"/></svg></span>
    00-000-0000
  </div>
</header>

<section class="hero">
  <svg class="hero-visual" viewBox="0 0 400 315" role="img" aria-label="Hexagon collage of photos showing hand and wrist examinations">
    <g stroke="#fff" stroke-width="5">
      <polygon points="195,15 245,15 270,58 245,101 195,101 170,58" fill="#9fb8cf"/>
      <polygon points="280,30 330,30 355,73 330,116 280,116 255,73" fill="#c9d7e4"/>
      <polygon points="115,95 185,95 220,155 185,215 115,215 80,155" fill="#d8b8a0"/>
      <polygon points="225,120 280,120 308,168 280,216 225,216 197,168" fill="#b9c9d8"/>
      <polygon points="130,225 175,225 198,263 175,301 130,301 107,263" fill="#a8c2d6"/>
    </g>
  </svg>
  <form class="lead-form">
    <h2>Get a <em>free</em> diagnosis</h2>
    <div class="field">Name</div>
    <div class="field">Phone</div>
    <div class="field">Email</div>
    <div class="field">Requested Appointment time</div>
    <button class="submit" type="button">Submit</button>
  </form>
</section>

<section class="about">
  <h2>What is <span>Carpal Tunnel Syndrome</span></h2>
  <div class="about-art" role="img" aria-label="Illustration of a hand showing the carpal tunnel"></div>
  <div class="about-text">
    <p>In Dr. Halvern's clinical practice, Carpal Tunnel Syndrome is one of the most commonly reported health problems. Carpal tunnel occurs when swelling pinches the median nerve, which provides sensation to the palm side of the thumb, index finger, middle finger and to the inside half of the ring finger.</p>
    <p>The result can be a combination of tingling, numbness, weakness and pain in the fingers, thumb, palm or the forearm. If the condition is not treated, permanent deterioration of muscle tissue can occur.</p>
  </div>
</section>

<section class="conditions">
  <h2>Other conditions treated by <span>Dr. Halvern</span></h2>
  <ul class="condition-list">
    <li><span class="num">1</span>Cubital Tunnel Syndrome</li>
    <li><span class="num">4</span>Hand Fractures</li>
    <li><span class="num">2</span>DeQuervain Tenosynovitis</li>
    <li><span class="num">5</span>Hand Sprains</li>
    <li><span class="num">3</span>Dupuytren's Disease</li>
  </ul>
  <div class="doctor-photo" role="img" aria-label="Portrait photo of the doctor"></div>
</section>

<section class="location">
  <div class="map" role="img" aria-label="Map showing the clinic location"></div>
  <div class="address">
    <h3>Corporate Address:</h3>
    <div class="address-row">
      <svg width="10" height="12" viewBox="0 0 24 30"><path fill="#1e8ee0" d="M12 0a10 10 0 0 0-10 10c0 7.5 10 20 10 20s10-12.5 10-20A10 10 0 0 0 12 0zm0 14a4 4 0 1 1 0-8 4 4 0 0 1 0 8z"/></svg>
      <div>Lorem ipsum is simply dummy<br>There are many variations of passages,<br>Readable content<br>Pincode - 00000000</div>
    </div>
    <div class="address-row">
      <svg width="11" height="9" viewBox="0 0 24 18"><path fill="#1e8ee0" d="M0 0h24v18H0zM2 2l10 7 10-7z" fill-rule="evenodd"/></svg>
      <div>hello@halvernhand.com</div>
    </div>
    <div class="address-row">
      <svg width="11" height="11" viewBox="0 0 24 24"><path fill="#1e8ee0" d="M6.6 10.8a15.1 15.1 0 0 0 6.6 6.6l2.2-2.2c.3-.3.7-.4 1-.2 1.1.4 2.3.6 3.6.6.6 0 1 .4 1 1V20c0 .6-.4 1-1 1A17 17 0 0 1 3 4c0-.6.4-1 1-1h3.5c.6 0 1 .4 1 1 0 1.3.2 2.5.6 3.6.1.3 0 .7-.2 1z"/></svg>
      <div>+10 5550100 / 22 / 33 / 44</div>
    </div>
  </div>
</section>

<footer class="site-footer">© 2000 - 2015 Dr. Halvern. All Rights Reserved</footer>

</body>
</html>
```